Velmora Link needs a brochure review

We are a company operating in more than 10 countries that, since 1972, has the ambitious and innovative objective to stimulate foreign language learning by discovering different countries and cultures, through training courses tailored to individual needs
We need a layout review of our brochure in order to make the content clearer, immediate and appealing and, at the same time, make the layout more modern and young.
The pages we need are: the cover and pages 3, 5, 7, 20, 21, 22, 23, 34, 36, 37. You will find our actual brochure pdf as attachment

Target Market(s)

Students and families, business

Industry/Entity Type

It Company

Requirements
Must have
• The same written information as the actual one.
• Blue and green colours.
• The cover must be simple, elegant and clean but new and effective. In addition to the cover the pages you should review are number :2, 3, 4, 5, 6, 7. Feel free to use new background, images and new layout for the text.

```html
<!DOCTYPE html>
<html lang="it">
<head>
<meta charset="utf-8">
<title>Velmora Link – Vacanze Studio 2017</title>
<link href="https://fonts.googleapis.com/css2?family=PT+Sans+Narrow:wght@400;700&family=Cabin:wght@400;600&display=swap" rel="stylesheet">
<style>
  :root {
    --green: #2a9038;
    --navy: #245480;
    --navy-dark: #1f3f63;
    --ink: #2f2f2f;
    --paper: #ffffff;
    --stage: #e4e4e4;
    --photo-a: #c9b7a6;
    --photo-b: #6d5a52;
    --photo-c: #e3c2c6;
    --photo-d: #b86b55;
  }
  * { margin: 0; padding: 0; box-sizing: border-box; }
  html, body { width: 960px; height: 1200px; overflow: hidden; background: var(--stage); }
  body { font-family: "Cabin", sans-serif; color: var(--ink); }

  .spread {
    position: absolute; left: 40px; top: 300px;
    width: 880px; height: 600px; display: flex;
  }
  .page {
    position: relative; width: 440px; height: 600px;
    background: var(--paper); overflow: hidden;
  }
  .page-art { position: absolute; inset: 0; width: 440px; height: 600px; }

  .brand {
    position: absolute; display: flex; align-items: center; justify-content: center;
    border-radius: 50%; color: #fff; font-family: "Cabin", sans-serif;
    font-weight: 600; text-align: center; line-height: 1;
  }
  .brand--back { left: 21px; top: 8px; width: 158px; height: 158px; background: var(--green); font-size: 24px; }
  .brand--front { left: 24px; top: 10px; width: 120px; height: 120px; background: var(--navy); font-size: 17px; box-shadow: 0 0 0 3px #fff, 0 0 0 5px var(--navy); }

  /* back cover contacts */
  .contact-title {
    position: absolute; left: 14px; top: 496px;
    font-size: 7px; font-weight: 600; color: var(--navy-dark); letter-spacing: .2px;
  }
  .office { position: absolute; font-size: 6.5px; line-height: 13px; color: var(--ink); }
  .office--milano { left: 14px; top: 514px; }
  .office--roma { left: 134px; top: 510px; }
  .office--web { left: 334px; top: 512px; }
  .office h4 { font-size: 7.5px; font-weight: 600; }
  .office li { list-style: none; display: flex; align-items: center; gap: 5px; }
  .ico { width: 8px; height: 8px; flex: none; }
  .partners { position: absolute; right: 12px; top: 552px; display: flex; gap: 6px; align-items: center; }
  .partner { width: 18px; height: 16px; background: #c8ccd3; border-radius: 2px; }
  .partner--wide { width: 60px; height: 14px; background: #d4d6da; }

  /* front cover */
  .season {
    position: absolute; right: 14px; top: 12px; text-align: right; color: #fff;
  }
  .season h2 { font-family: "Cabin", sans-serif; font-weight: 400; font-size: 17px; }
  .season p { font-size: 6.5px; line-height: 9px; text-transform: uppercase; }

  .headline { position: absolute; left: 20px; top: 410px; font-family: "PT Sans Narrow", sans-serif; line-height: 1; }
  .headline .lead { display: block; font-size: 38px; color: #3a3a3a; font-weight: 400; }
  .headline .main { display: block; font-size: 44px; color: var(--navy); font-weight: 700; margin-top: 4px; }

  .badge {
    position: absolute; left: 290px; top: 418px; width: 140px; height: 140px;
    border-radius: 50%; background: #fff; border: 4px solid var(--green);
    display: flex; flex-direction: column; align-items: center; justify-content: center;
    font-family: "PT Sans Narrow", sans-serif; font-weight: 700; font-size: 20px; line-height: 24px;
    box-shadow: 0 6px 6px -4px rgba(0,0,0,.25);
  }
  .badge .accent { color: var(--navy); }
  .badge .dark { color: #2b2b2b; }

  .facts { position: absolute; top: 518px; font-size: 8px; line-height: 10px; }
  .facts h5 { font-weight: 400; text-transform: uppercase; letter-spacing: .3px; }
  .facts p { font-weight: 600; }
  .facts--dest { left: 30px; }
  .facts--prog { left: 168px; }
  .facts-rule { position: absolute; left: 148px; top: 508px; width: 1px; height: 50px; background: #9a9a9a; }
</style>
</head>
<body>
<main class="spread">

  <!-- back cover -->
  <section class="page page--back">
    <svg class="page-art" viewBox="0 0 440 600">
      <defs>
        <linearGradient id="groupTone" x1="0" y1="0" x2="0" y2="1">
          <stop offset="0" stop-color="#ffffff"/>
          <stop offset=".3" stop-color="#e7e4df"/>
          <stop offset=".55" stop-color="var(--photo-a)"/>
          <stop offset="1" stop-color="var(--photo-b)"/>
        </linearGradient>
        <linearGradient id="footFade" x1="0" y1="0" x2="0" y2="1">
          <stop offset="0" stop-color="#ffffff"/>
          <stop offset="1" stop-color="#e6e6e6"/>
        </linearGradient>
      </defs>
      <rect x="0" y="440" width="440" height="160" fill="url(#footFade)"/>
      <path role="img" aria-label="Photo of a smiling group of teenage friends hugging outdoors"
            d="M0,80 L440,80 L440,452 Q220,462 0,473 Z"
            fill="url(#groupTone)"/>
      <path d="M0,473 Q220,462 440,452" fill="none" stroke="var(--navy)" stroke-width="4"/>
      <path d="M0,271 C8,150 100,22 214,0" fill="none" stroke="var(--green)" stroke-width="5"/>
    </svg>

    <div class="brand brand--back">Velmora Link</div>

    <p class="contact-title">PER INFORMAZIONI E PRENOTAZIONI</p>

    <div class="office office--milano">
      <h4>Milano</h4>
      <ul>
        <li><svg class="ico" viewBox="0 0 10 10"><circle cx="5" cy="5" r="5" fill="var(--navy)"/><circle cx="5" cy="4.3" r="1.6" fill="#fff"/></svg>20121 - Via Lorenzi, 14</li>
        <li><svg class="ico" viewBox="0 0 10 10"><circle cx="5" cy="5" r="5" fill="var(--navy)"/><path d="M3.2 2.8l1 1-0.6 .8c.4.8 1 1.4 1.8 1.8l.8-.6 1 1-.7.9c-2-.4-3.8-2.2-4.2-4.2z" fill="#fff"/></svg>+39 02 44182200</li>
        <li><svg class="ico" viewBox="0 0 10 10"><circle cx="5" cy="5" r="5" fill="var(--navy)"/><rect x="2.8" y="3.5" width="4.4" height="3" fill="#fff"/></svg>+39 02 441822099</li>
      </ul>
    </div>

    <div class="office office--roma">
      <h4>Roma</h4>
      <ul>
        <li><svg class="ico" viewBox="0 0 10 10"><circle cx="5" cy="5" r="5" fill="var(--navy)"/><circle cx="5" cy="4.3" r="1.6" fill="#fff"/></svg>00153 - Via Carlo Melzi 9</li>
        <li><svg class="ico" viewBox="0 0 10 10"><circle cx="5" cy="5" r="5" fill="var(--navy)"/><path d="M3.2 2.8l1 1-0.6 .8c.4.8 1 1.4 1.8 1.8l.8-.6 1 1-.7.9c-2-.4-3.8-2.2-4.2-4.2z" fill="#fff"/></svg>+39 06 57310400</li>
        <li><svg class="ico" viewBox="0 0 10 10"><circle cx="5" cy="5" r="5" fill="var(--navy)"/><rect x="2.8" y="3.5" width="4.4" height="3" fill="#fff"/></svg>+39 06 57310499</li>
      </ul>
    </div>

    <div class="office office--web">
      <ul>
        <li><svg class="ico" viewBox="0 0 10 10"><circle cx="5" cy="5" r="4.3" fill="none" stroke="var(--navy)" stroke-width="1.2"/><path d="M3 4l2 1.4L7 4" fill="none" stroke="var(--navy)" stroke-width="1"/></svg>info@velmoralink.it</li>
        <li><svg class="ico" viewBox="0 0 10 10"><circle cx="5" cy="5" r="4.3" fill="none" stroke="var(--navy)" stroke-width="1.2"/><path d="M0.8 5h8.4M5 .8v8.4" stroke="var(--navy)" stroke-width=".9"/></svg>www.velmoralink.it</li>
      </ul>
    </div>

    <div class="partners" aria-label="Partner accreditations">
      <span class="partner"></span><span class="partner"></span><span class="partner"></span><span class="partner partner--wide"></span>
    </div>
  </section>

  <!-- front cover -->
  <section class="page page--front">
    <svg class="page-art" viewBox="0 0 440 600">
      <defs>
        <linearGradient id="summerTone" x1="0" y1="0" x2="1" y2="1">
          <stop offset="0" stop-color="#f1ece4"/>
          <stop offset=".4" stop-color="var(--photo-c)"/>
          <stop offset="1" stop-color="var(--photo-d)"/>
        </linearGradient>
        <linearGradient id="coverFade" x1="0" y1="0" x2="0" y2="1">
          <stop offset="0" stop-color="#ffffff"/>
          <stop offset="1" stop-color="#e4e4e4"/>
        </linearGradient>
      </defs>
      <rect width="440" height="600" fill="url(#coverFade)"/>
      <path d="M180,0 C320,60 420,190 440,338 L440,0 Z" fill="var(--navy)"/>
      <path role="img" aria-label="Photo of two smiling girls in sun hats and sunglasses on a summer street"
            d="M10,103 L296,103 C366,160 422,250 440,352 L440,482 C300,470 150,420 10,313 Z"
            fill="url(#summerTone)"/>
      <path d="M10,313 C150,420 300,470 440,482" fill="none" stroke="var(--green)" stroke-width="5"/>
    </svg>

    <div class="brand brand--front">Velmora Link</div>

    <div class="season">
      <h2>Vacanze Studio 2017</h2>
      <p>Dai 10 ai 18 anni</p>
      <p>Di gruppo con accompagnatore</p>
    </div>

    <h1 class="headline">
      <span class="lead">L’ESTATE</span>
      <span class="main">CHE SOGNI</span>
    </h1>

    <div class="badge">
      <span class="accent">PREZZI</span>
      <span class="accent">BLOCCATI</span>
      <span class="dark">LIBERI DI</span>
      <span class="dark">RIPENSARCI</span>
    </div>

    <div class="facts facts--dest">
      <h5>Destinazioni:</h5>
      <p>Irlanda, Gran Bretagna</p>
      <p>Stati Uniti, Malta</p>
    </div>
    <span class="facts-rule"></span>
    <div class="facts facts--prog">
      <h5>Programmi:</h5>
      <p>Rugby, Calcio, Surf</p>
      <p>Equitazione, Danza</p>
    </div>
  </section>

</main>
</body>
</html>
```